Website for company called VORENTbio

We need a website for our new company called VORENTbio which developed a platform/technology to identify antigen-specific T cells (immune cells) which can be used for cancer therapy, autoimmunity, etc.

The platform is called VORENT and is rapid, versatile, unbiased, and inexpensive.

We have a semi-final logo although we are not completely set on color and font of text (attached).

Target Market(s)

Our target audience at the moment would be potential investors and VCs. We eventually are interested in getting attention from scientists and cell/immunotherapy companies.

Industry/Entity Type

Healthcare/Technology

Coding

Coded - Design and coding required

Number of Pages Required

1 page

Colors
0094D4
00A9DD
6FCCEA
C7EBF8
E9F6FB
00AB8E
00BBA5
67D7C9
C6EFE9
E9F9F6
E54698
E96AAD
F1A4CE
F9D9EA
FCEFF6
A7469A
B969AE
D3A5CF
EDDBEB
F8F0F9
6B429C
8869AF
B7A5CE
E3DAEB
F3F0F8

Requirements
Must have
• Landing page about the company, About us page, Technology page (could be merged with company landing page), Contact us page

```html
<!DOCTYPE html>
<html lang="en">
<head>
<meta charset="UTF-8">
<title>VORENTbio — Antigen-Specific T Cells</title>
<link rel="stylesheet" href="https://fonts.googleapis.com/css2?family=Montserrat:wght@500;600;700&family=Inter:wght@400;500;600&display=swap">
<style>
  :root{
    --cyan:#00BFF3;
    --cyan-soft:#1fc6f2;
    --blue-deep:#0094D4;
    --blue-mid:#00A9DD;
    --blue-light:#6FCCEA;
    --ink:#111111;
    --text:#2a2a2a;
    --white:#ffffff;
    --black:#000000;
    --purple:#A7469A;
    --violet:#6B429C;
    --pink:#E54698;
    --navy:#1b2446;
  }
  *{box-sizing:border-box;margin:0;padding:0}
  html,body{width:1200px;height:2470px;overflow:hidden}
  body{position:relative;background:var(--white);font-family:'Inter',sans-serif;color:var(--text)}
  .heading{font-family:'Montserrat',sans-serif}
  .abs{position:absolute}

  /* Hero */
  .hero{position:absolute;left:0;top:0;width:1200px;height:590px;
    background:radial-gradient(circle at 30% 20%,#3fd0f7 0%,transparent 40%),
               radial-gradient(circle at 85% 45%,#0aa3d9 0%,transparent 45%),
               linear-gradient(180deg,#19bff0 0%,#0ea8e0 60%,#0b9fd8 100%)}
  .hero-wave{position:absolute;left:0;top:470px;width:1200px;height:125px}
  .brand{font-family:'Montserrat',sans-serif;font-weight:700;font-size:25px;color:var(--white);letter-spacing:-.2px}
  .nav{position:absolute;left:620px;top:34px;display:flex;gap:6px;align-items:center}
  .nav a{font-family:'Montserrat',sans-serif;font-size:13.5px;font-weight:500;color:var(--white);text-decoration:none;padding:10px 20px;border-radius:20px}
  .nav a.active{background:var(--black);font-weight:700}
  .hero-title{position:absolute;left:0;top:172px;width:1200px;text-align:center;font-family:'Montserrat',sans-serif;font-weight:700;font-size:44px;line-height:50px;color:var(--white)}
  .hero-sub{position:absolute;left:260px;top:287px;width:680px;text-align:center;font-size:16.5px;line-height:24px;color:var(--white);font-weight:500}
  .btn{position:absolute;display:flex;align-items:center;justify-content:center;border-radius:22px;font-family:'Montserrat',sans-serif;font-weight:700;font-size:13.5px;color:var(--white);text-decoration:none;background:var(--black)}
  .btn-cyan{background:var(--cyan-soft)}

  /* Sections */
  .section-title{font-family:'Montserrat',sans-serif;font-weight:700;font-size:31px;color:var(--cyan)}
  .section-sub{font-family:'Montserrat',sans-serif;font-weight:700;font-size:20px;line-height:23px;color:var(--ink)}
  .body-copy{font-size:16px;line-height:24px;color:var(--text)}
  .photo-circle{position:absolute;border-radius:50%;overflow:hidden}
  .ring{position:absolute;border-radius:50%;border:2px solid var(--white)}

  .features{position:absolute;left:612px;top:1275px;list-style:none}
  .features li{position:relative;padding-left:28px;margin-bottom:13px}
  .features svg{position:absolute;left:0;top:3px}
  .features strong{display:block;font-weight:600;font-size:17px;color:var(--ink);line-height:24px}
  .features span{display:block;font-size:14.5px;color:var(--text);line-height:22px;margin-top:2px}

  /* Contact */
  .contact{position:absolute;left:0;top:1633px;width:1200px;height:555px;
    background:radial-gradient(circle at 78% 45%,#27b7e6 0%,transparent 40%),
               radial-gradient(circle at 15% 80%,#1aa3d6 0%,transparent 45%),
               linear-gradient(180deg,#15a6dc 0%,#129fd6 100%)}
  .field{position:absolute;left:138px;width:452px;height:41px;border:1px solid var(--white);color:var(--white);font-size:13.5px;padding:12px 14px;background:transparent}

  /* Footer */
  .footer{position:absolute;left:0;top:2187px;width:1200px;height:283px;background:var(--black);color:var(--white)}
  .foot-title{position:absolute;top:47px;font-family:'Montserrat',sans-serif;font-weight:700;font-size:20px;color:var(--cyan)}
  .foot-list{position:absolute;list-style:none;font-family:'Montserrat',sans-serif;font-size:13.5px;font-weight:500}
  .foot-list li{position:relative;height:24px;padding-left:30px;line-height:20px}
  .foot-list svg{position:absolute;left:0;top:4px}
  .foot-contact{position:absolute;left:145px;font-family:'Montserrat',sans-serif;font-size:12.5px;line-height:14px}
  .foot-contact svg{position:absolute;left:0;top:0}
  .foot-contact p{padding-left:29px}
  .copyright{position:absolute;left:0;top:2431px;width:1200px;text-align:center;font-family:'Montserrat',sans-serif;font-size:13px;color:var(--white)}
</style>
</head>
<body>

<header class="hero" role="img" aria-label="Blurred blue microscopic view of floating immune cells">
  <div class="brand abs" style="left:143px;top:30px">VORENTbio</div>
  <nav class="nav">
    <a class="active" href="#home">Home</a>
    <a href="#about">About Us</a>
    <a href="#technology">Technology</a>
    <a href="#contact">Contact Us</a>
  </nav>
  <h1 class="hero-title">Unlocking the Power of<br>Antigen-Specific T Cells</h1>
  <p class="hero-sub">A transformative platform to identify and harness antigen-specific T cells for targeted therapies in cancer, autoimmunity, infectious diseases, and beyond.</p>
  <a class="btn btn-cyan" href="#technology" style="left:412px;top:363px;width:210px;height:41px">Explore Our Technology</a>
  <a class="btn" href="#contact" style="left:627px;top:363px;width:162px;height:41px">Partner With Us</a>
</header>
<svg class="hero-wave" viewBox="0 0 1200 125" preserveAspectRatio="none" aria-hidden="true">
  <path d="M0 100 C60 60 120 15 170 15 C230 15 250 70 340 95 C420 115 480 35 560 28 C640 22 680 90 760 108 C840 125 900 50 980 30 C1060 12 1130 40 1200 110 L1200 125 L0 125 Z" fill="#ffffff"/>
</svg>

<section id="about">
  <h2 class="section-title abs" style="left:143px;top:656px">About VORENTbio</h2>
  <h3 class="section-sub abs" style="left:142px;top:702px">Engineering Precision into Immunotherapy</h3>
  <p class="body-copy abs" style="left:140px;top:744px;width:440px">VORENTbio is a biotechnology company pioneering a platform to identify and isolate antigen-specific T cells from patients. Our technology enables deep profiling of T cell-antigen interactions, unlocking new pathways for therapeutic development across oncology, autoimmunity, and infectious disease.</p>
  <a class="btn" href="#about" style="left:135px;top:910px;width:125px;height:41px">Learn More</a>
  <div class="photo-circle" style="left:650px;top:597px;width:407px;height:407px;background:radial-gradient(circle at 55% 45%,#b43fb5 0%,#5a3f9e 22%,#2f5c8a 45%,#1f2b4a 75%,#141a30 100%)" role="img" aria-label="Illustration of a purple immune cell surrounded by floating particles"></div>
  <div class="ring" style="left:666px;top:599px;width:407px;height:407px;border-color:var(--white);clip-path:inset(0 60% 0 0)"></div>
</section>

<section id="technology">
  <div class="photo-circle" style="left:135px;top:1118px;width:407px;height:407px;background:radial-gradient(circle at 45% 50%,#ff5a4a 0%,#b2306a 18%,#3b2f8a 45%,#1d2d6a 75%,#0f1844 100%)" role="img" aria-label="Illustration of a glowing T cell on a digital circuit surface"></div>
  <div class="ring" style="left:115px;top:1116px;width:407px;height:407px;clip-path:inset(0 0 0 60%)"></div>
  <h2 class="section-title abs" style="left:612px;top:1068px">Our Technology</h2>
  <h3 class="section-sub abs" style="left:613px;top:1113px;width:420px">VORENT: Antigen-T Cell Capture &amp; Characterization</h3>
  <p class="body-copy abs" style="left:613px;top:1166px;width:450px">A proprietary platform for high-throughput identification of antigen-specific T cells.</p>
  <h4 class="abs" style="left:612px;top:1233px;font-weight:600;font-size:19px;color:var(--cyan)">Features</h4>
  <ul class="features">
    <li><svg width="16" height="16" viewBox="0 0 16 16" aria-hidden="true"><circle cx="8" cy="8" r="7.5" fill="var(--cyan)"/><path d="M4.5 8.2 7 10.5 11.5 5.8" stroke="#fff" stroke-width="1.8" fill="none"/></svg><strong>High Sensitivity &amp; Specificity</strong><span>Detect rare, disease-relevant T cells.</span></li>
    <li><svg width="16" height="16" viewBox="0 0 16 16" aria-hidden="true"><circle cx="8" cy="8" r="7.5" fill="var(--cyan)"/><path d="M4.5 8.2 7 10.5 11.5 5.8" stroke="#fff" stroke-width="1.8" fill="none"/></svg><strong>Multiplexed Antigen Screening</strong><span>Profile T cell responses to hundreds of targets simultaneously.</span></li>
    <li><svg width="16" height="16" viewBox="0 0 16 16" aria-hidden="true"><circle cx="8" cy="8" r="7.5" fill="var(--cyan)"/><path d="M4.5 8.2 7 10.5 11.5 5.8" stroke="#fff" stroke-width="1.8" fill="none"/></svg><strong>Scalable Cell Isolation</strong><span>Recover viable, functional T cells for downstream use.</span></li>
    <li><svg width="16" height="16" viewBox="0 0 16 16" aria-hidden="true"><circle cx="8" cy="8" r="7.5" fill="var(--cyan)"/><path d="M4.5 8.2 7 10.5 11.5 5.8" stroke="#fff" stroke-width="1.8" fill="none"/></svg><strong>Single-Cell Resolution</strong><span>Integrate TCR sequencing with antigen recognition.</span></li>
  </ul>
  <a class="btn" href="#technology" style="left:618px;top:1521px;width:125px;height:41px">Learn More</a>
</section>

<section id="contact" class="contact" role="img" aria-label="Blurred blue background of immune cells">
  <h2 class="heading abs" style="left:139px;top:68px;font-weight:700;font-size:31px;color:var(--white)">Contact Us</h2>
  <div class="field" style="top:132px">Name</div>
  <div class="field" style="top:189px">Email</div>
  <div class="field" style="top:246px">Phone</div>
  <div class="field" style="top:303px;height:122px">Message</div>
  <a class="btn" href="#contact" style="left:135px;top:445px;width:125px;height:41px">Submit</a>
  <div class="abs" style="left:695px;top:88px;width:380px;height:370px;border-radius:48% 52% 45% 55%/50% 45% 55% 50%;background:radial-gradient(circle at 48% 50%,#d23ab8 0%,#8a3fb0 35%,#4f68c8 65%,#3a7fd0 100%)" role="img" aria-label="Illustration of a ruffled purple and blue T cell"></div>
</section>

<footer class="footer">
  <h3 class="foot-title" style="left:145px">Address</h3>
  <div class="foot-contact" style="top:95px">
    <svg width="13" height="16" viewBox="0 0 13 16" aria-hidden="true"><path d="M6.5 0C3 0 .5 2.6.5 5.8 .5 10 6.5 16 6.5 16s6-6 6-10.2C12.5 2.6 10 0 6.5 0Zm0 8.2a2.3 2.3 0 1 1 0-4.6 2.3 2.3 0 0 1 0 4.6Z" fill="#fff"/></svg>
    <p>#123,Lorium ipsum dolor<br>amit, city name.NJ</p>
  </div>
  <div class="foot-contact" style="top:137px">
    <svg width="16" height="16" viewBox="0 0 16 16" aria-hidden="true"><path d="M3.3 0.8 5.6 3.5 4.4 5.6c.9 2 2.6 3.8 4.6 4.8l2.1-1.2 2.8 2.3-1 3C7.2 14.3 1.8 8.9 0.6 2.1Z" fill="#fff"/></svg>
    <p>1-800 555 0142</p>
  </div>
  <div class="foot-contact" style="top:172px">
    <svg width="15" height="12" viewBox="0 0 15 12" aria-hidden="true" style="top:2px"><rect width="15" height="12" rx="1" fill="#fff"/><path d="M0.5 1 7.5 6.5 14.5 1" stroke="#000" stroke-width="1.3" fill="none"/></svg>
    <p>hello@vorentbio.com</p>
  </div>

  <h3 class="foot-title" style="left:416px">Quick Links</h3>
  <ul class="foot-list" style="left:416px;top:92px">
    <li><svg width="8" height="11" viewBox="0 0 8 11" aria-hidden="true"><path d="M1.5 1 6 5.5 1.5 10" stroke="#fff" stroke-width="1.8" fill="none"/></svg>Home</li>
    <li><svg width="8" height="11" viewBox="0 0 8 11" aria-hidden="true"><path d="M1.5 1 6 5.5 1.5 10" stroke="#fff" stroke-width="1.8" fill="none"/></svg>About Us</li>
    <li><svg width="8" height="11" viewBox="0 0 8 11" aria-hidden="true"><path d="M1.5 1 6 5.5 1.5 10" stroke="#fff" stroke-width="1.8" fill="none"/></svg>Technology</li>
    <li><svg width="8" height="11" viewBox="0 0 8 11" aria-hidden="true"><path d="M1.5 1 6 5.5 1.5 10" stroke="#fff" stroke-width="1.8" fill="none"/></svg>Contact Us</li>
  </ul>

  <h3 class="foot-title" style="left:657px">Follow us</h3>
  <ul class="foot-list" style="left:657px;top:92px">
    <li><svg width="11" height="11" viewBox="0 0 11 11" aria-hidden="true"><circle cx="5.5" cy="5.5" r="5" fill="#fff"/></svg>Feedspace</li>
    <li><svg width="11" height="11" viewBox="0 0 11 11" aria-hidden="true"><circle cx="5.5" cy="5.5" r="5" fill="#fff"/></svg>Snapgram</li>
    <li><svg width="11" height="11" viewBox="0 0 11 11" aria-hidden="true"><circle cx="5.5" cy="5.5" r="5" fill="#fff"/></svg>Chirper</li>
    <li><svg width="11" height="11" viewBox="0 0 11 11" aria-hidden="true"><circle cx="5.5" cy="5.5" r="5" fill="#fff"/></svg>WorkLink</li>
  </ul>

  <div class="brand abs" style="left:870px;top:114px">VORENTbio</div>
</footer>
<p class="copyright">© 2025 | www.vorentbio.com</p>

</body>
</html>
```